Social Media Graphics - ALL TEXT RK

We are looking for a series of social media graphics for Instagram (standard size 1:1 (1080x1080px) that are ALL TEXT. We want the following quotes below on each graphic; one quote per graphic. AND, In very small letters at the bottom of each graphic, add @RKMarlowLive

The look and feel of these graphics should be complimentary to the color palette attached below; but keep them simple. But the design is up to you; at the end of this document, I provided various samples of all text graphics that I like as examples.

Target Market(s)

women looking to lose weight

Industry/Entity Type

health and wellness

Colors
E54698
E96AAD
F1A4CE
F9D9EA
FCEFF6

Requirements
Must have
• the quotes in the document
Should not have
• no stock photography

```html
<!DOCTYPE html>
<html lang="en">
<head>
<meta charset="utf-8">
<title>RK Social Graphics Series</title>
<link rel="stylesheet" href="https://fonts.googleapis.com/css2?family=Bebas+Neue&family=Oswald:wght@300&display=swap">
<style>
  :root {
    --pink-deep: #c23a86;
    --pink: #e54698;
    --pink-mid: #e96aad;
    --pink-soft: #f1a4ce;
    --pink-pale: #f9d9ea;
    --blush: #fceff6;
    --white: #ffffff;
    --canvas: #ffffff;
    --tile: 258px;
  }
  * { margin: 0; padding: 0; box-sizing: border-box; }
  html, body {
    width: 1200px; height: 912px; overflow: hidden;
    background: var(--canvas);
  }
  .series { position: relative; width: 1200px; height: 912px; }
  .post {
    position: absolute;
    width: var(--tile); height: var(--tile);
    overflow: hidden;
    box-shadow: 0 1px 3px rgba(0,0,0,.25);
  }
  .post__photo { position: absolute; inset: 0; }
  .post__shapes { position: absolute; inset: 0; width: 100%; height: 100%; }
  .post__quote {
    position: absolute; right: 10px; bottom: 14px;
    font-family: "Bebas Neue", sans-serif;
    font-size: 20px; line-height: 23px;
    color: var(--white); text-align: right;
    white-space: nowrap;
    text-shadow: 0 1px 2px rgba(0,0,0,.25);
  }
  .post__quote--dense { font-size: 18px; line-height: 20px; }
  .post__quote--compact { font-size: 16px; line-height: 17px; }
  .post__quote--raised { bottom: 36px; }
  .post__quote--lifted { bottom: 27px; }
  .post__quote--nudged { bottom: 22px; }
  .post__handle {
    position: absolute; left: 28px; bottom: 8px;
    font-family: "Oswald", sans-serif; font-weight: 300;
    font-size: 14px; line-height: 16px; color: var(--white);
    text-shadow: 0 1px 2px rgba(0,0,0,.2);
  }
  .photo--gala { background: linear-gradient(135deg, #6a4aa0 0%, #c0408e 50%, #e05aa6 100%); }
  .photo--studio { background: linear-gradient(150deg, #e8ddd0 0%, #c79a78 55%, #7a4a32 100%); }
  .photo--arena { background: linear-gradient(160deg, #3a3a3a 0%, #8a7a6a 55%, #b58a6a 100%); }
  .photo--kitchen { background: linear-gradient(150deg, #e6e6e6 0%, #cfcfcf 50%, #2a2a2a 100%); }
  .photo--ball { background: linear-gradient(150deg, #bdb6b0 0%, #9a8dc8 55%, #d0a8e8 100%); }
  .photo--loft { background: linear-gradient(150deg, #cfcfcf 0%, #6a6a6a 55%, #1e1e1e 100%); }
  .photo--window { background: linear-gradient(150deg, #9a9a9a 0%, #3a3a3a 55%, #1a1a1a 100%); }
  .photo--lounge { background: linear-gradient(150deg, #2a2a2a 0%, #6a5a5a 55%, #e8c8d8 100%); }
  .photo--hills { background: linear-gradient(170deg, #e8eef2 0%, #a8aaa4 40%, #2a2a2a 100%); }
</style>
</head>
<body>
<main class="series">

  <article class="post" style="left:54px; top:30px;">
    <div class="post__photo photo--gala" role="img" aria-label="Photo of the host in a pink gown at an awards event"></div>
    <svg class="post__shapes" viewBox="0 0 258 258" aria-hidden="true">
      <polygon points="0,258 258,0 258,258" fill="var(--pink)" opacity=".72"/>
      <polygon points="0,0 40,0 0,40" fill="var(--pink-deep)" opacity=".85"/>
      <polygon points="40,0 56,0 0,56 0,40" fill="var(--pink-soft)" opacity=".6"/>
    </svg>
    <p class="post__quote">Wake up<br>tomorrow with a<br>flatter belly- yes, this<br>overnight remedy works<br>like magic!</p>
    <span class="post__handle">@RKMarlowLive</span>
  </article>

  <article class="post" style="left:330px; top:30px;">
    <div class="post__photo photo--studio" role="img" aria-label="Photo of the host smiling in a tan turtleneck"></div>
    <svg class="post__shapes" viewBox="0 0 258 258" aria-hidden="true">
      <polygon points="0,258 258,0 258,258" fill="var(--pink)" opacity=".72"/>
      <polygon points="0,0 40,0 0,40" fill="var(--pink-deep)" opacity=".85"/>
      <polygon points="40,0 56,0 0,56 0,40" fill="var(--pink-soft)" opacity=".6"/>
    </svg>
    <p class="post__quote">Struggling with<br>bloating and belly<br>fat? Try this natural<br>solution tonight, and wake<br>up feeling lighter!</p>
    <span class="post__handle">@RKMarlowLive</span>
  </article>

  <article class="post" style="left:606px; top:30px;">
    <div class="post__photo photo--arena" role="img" aria-label="Photo of the host courtside at a basketball arena"></div>
    <svg class="post__shapes" viewBox="0 0 258 258" aria-hidden="true">
      <polygon points="0,258 258,0 258,258" fill="var(--pink)" opacity=".72"/>
      <polygon points="0,0 40,0 0,40" fill="var(--pink-deep)" opacity=".85"/>
      <polygon points="40,0 56,0 0,56 0,40" fill="var(--pink-soft)" opacity=".6"/>
    </svg>
    <p class="post__quote post__quote--dense post__quote--lifted">A natural way to<br>boost GLP-1 - no<br>injections, no side effects,<br>just real results.<br>Here's how it works</p>
    <span class="post__handle">@RKMarlowLive</span>
  </article>

  <article class="post" style="left:882px; top:30px;">
    <div class="post__photo photo--kitchen" role="img" aria-label="Photo of the host dancing in a kitchen"></div>
    <svg class="post__shapes" viewBox="0 0 258 258" aria-hidden="true">
      <polygon points="0,258 258,0 258,258" fill="var(--pink)" opacity=".72"/>
      <polygon points="0,0 40,0 0,40" fill="var(--pink-deep)" opacity=".85"/>
      <polygon points="40,0 56,0 0,56 0,40" fill="var(--pink-soft)" opacity=".6"/>
    </svg>
    <p class="post__quote">One supplement,<br>one night; your belly<br>bloat could be gone by<br>morning. Here's how it<br>works!</p>
    <span class="post__handle">@RKMarlowLive</span>
  </article>

  <article class="post" style="left:54px; top:327px;">
    <div class="post__photo photo--ball" role="img" aria-label="Photo of the host beside a giant signed basketball"></div>
    <svg class="post__shapes" viewBox="0 0 258 258" aria-hidden="true">
      <polygon points="0,258 258,0 258,258" fill="var(--pink)" opacity=".72"/>
      <polygon points="0,0 40,0 0,40" fill="var(--pink-deep)" opacity=".85"/>
      <polygon points="40,0 56,0 0,56 0,40" fill="var(--pink-soft)" opacity=".6"/>
    </svg>
    <p class="post__quote post__quote--raised">You've been lied to<br>- 'just eat less and<br>exercise more' doesn't<br>work in menopause</p>
    <span class="post__handle">@RKMarlowLive</span>
  </article>

  <article class="post" style="left:330px; top:327px;">
    <div class="post__photo photo--loft" role="img" aria-label="Photo of the host in a sheer black top in a loft"></div>
    <svg class="post__shapes" viewBox="0 0 258 258" aria-hidden="true">
      <polygon points="0,258 258,0 258,258" fill="var(--pink)" opacity=".72"/>
      <polygon points="0,0 40,0 0,40" fill="var(--pink-deep)" opacity=".85"/>
      <polygon points="40,0 56,0 0,56 0,40" fill="var(--pink-soft)" opacity=".6"/>
    </svg>
    <p class="post__quote post__quote--dense post__quote--lifted">Frustrated with<br>belly fat that won't<br>budge? I've got the solution<br>that finally worked for me-no<br>crazy diets required.</p>
    <span class="post__handle">@RKMarlowLive</span>
  </article>

  <article class="post" style="left:606px; top:327px;">
    <div class="post__photo photo--window" role="img" aria-label="Photo of the host by a city-view window"></div>
    <svg class="post__shapes" viewBox="0 0 258 258" aria-hidden="true">
      <polygon points="0,258 258,0 258,258" fill="var(--pink)" opacity=".72"/>
      <polygon points="0,0 40,0 0,40" fill="var(--pink-deep)" opacity=".85"/>
      <polygon points="40,0 56,0 0,56 0,40" fill="var(--pink-soft)" opacity=".6"/>
    </svg>
    <p class="post__quote post__quote--raised">Sis, your<br>hormones are out of<br>whack - that's why the<br>weight won't budge!</p>
    <span class="post__handle">@RKMarlowLive</span>
  </article>

  <article class="post" style="left:882px; top:327px;">
    <div class="post__photo photo--lounge" role="img" aria-label="Photo of the host posing in a lounge at night"></div>
    <svg class="post__shapes" viewBox="0 0 258 258" aria-hidden="true">
      <polygon points="0,258 258,0 258,258" fill="var(--pink)" opacity=".72"/>
      <polygon points="0,0 40,0 0,40" fill="var(--pink-deep)" opacity=".85"/>
      <polygon points="40,0 56,0 0,56 0,40" fill="var(--pink-soft)" opacity=".6"/>
    </svg>
    <p class="post__quote post__quote--raised">Hat stubborn<br>belly fat isn't your<br>fault - here's what no<br>one tells you.</p>
    <span class="post__handle">@RKMarlowLive</span>
  </article>

  <article class="post" style="left:330px; top:618px;">
    <div class="post__photo photo--hills" role="img" aria-label="Photo of the host outdoors with hills behind"></div>
    <svg class="post__shapes" viewBox="0 0 258 258" aria-hidden="true">
      <polygon points="0,258 258,0 258,258" fill="var(--pink)" opacity=".72"/>
      <polygon points="0,0 40,0 0,40" fill="var(--pink-deep)" opacity=".85"/>
      <polygon points="40,0 56,0 0,56 0,40" fill="var(--pink-soft)" opacity=".6"/>
    </svg>
    <p class="post__quote post__quote--compact post__quote--nudged">GLP-1:<br>The magic behind the weight<br>loss drugs.<br>But here's the secret<br>- you can boost it naturally without<br>a prescription!</p>
    <span class="post__handle">@RKMarlowLive</span>
  </article>

  <article class="post" style="left:606px; top:618px;">
    <div class="post__photo photo--hills" role="img" aria-label="Photo of the host in profile with hills behind"></div>
    <svg class="post__shapes" viewBox="0 0 258 258" aria-hidden="true">
      <polygon points="0,258 258,0 258,258" fill="var(--pink)" opacity=".72"/>
      <polygon points="0,0 40,0 0,40" fill="var(--pink-deep)" opacity=".85"/>
      <polygon points="40,0 56,0 0,56 0,40" fill="var(--pink-soft)" opacity=".6"/>
    </svg>
    <p class="post__quote post__quote--raised">Finally-a natural<br>solution that<br>flattens your belly and<br>eases stomach bloat</p>
    <span class="post__handle">@RKMarlowLive</span>
  </article>

</main>
</body>
</html>
```